e-commerce store for sport clothing online store "baseball merchandise "web application...

I want to design a UX/UI for my web application website for the online store I will provide you with the following:
1. screen shots of the initial design for the pages>
2. the logo files.
3. The brand guideline file.

the provided files (screen shots) is guideline I want to see CREATIVITY with the UX/UI DESIGN.
PS. PLEASE FOLLOW THE BRANDGUIDE LINE CAREFULLY SPECIALLY THE TYPOGRAPHY & THE COLOR CODES.

PLEASE VISIT THIS WEBSITE brightpin.lumar-qt.com to see more for the screens.

```html
<!DOCTYPE html>
<html lang="en">
<head>
<meta charset="utf-8">
<title>Diamond Nine Store Screens</title>
<link href="https://fonts.googleapis.com/css2?family=Poppins:wght@400;500;600&display=swap" rel="stylesheet">
<style>
:root{
  --stage:#fcae03;
  --navy:#0c2146;
  --crimson:#ad0f33;
  --panel:#ffffff;
  --bar:#f6f6f6;
  --ink:#1f1f1f;
  --muted:#6b6b6b;
  --line:#dcdcdc;
}
*{box-sizing:border-box;margin:0;padding:0}
html,body{width:884px;height:1200px;overflow:hidden;background:var(--stage);font-family:'Poppins',sans-serif;color:var(--ink)}
.screen{position:absolute;left:74px;width:736px;height:526px;background:var(--panel);box-shadow:0 4px 10px rgba(0,0,0,.12);overflow:hidden}
.screen.list{top:50px}
.screen.detail{top:624px}
.sidebar{position:absolute;left:0;top:0;width:124px;height:100%;background:var(--navy)}
.brand{position:absolute;left:0;top:22px;width:124px;text-align:center;color:#fff;font-weight:600;font-size:13px;display:flex;align-items:center;justify-content:center;gap:6px}
.brand-dot{width:10px;height:10px;border-radius:50%;background:var(--crimson)}
.menu{position:absolute;top:88px;left:0;width:124px;list-style:none}
.menu li{height:30px;line-height:30px;padding-left:13px;font-size:9px;color:#fff}
.menu li.active{background:var(--crimson);height:32px;line-height:32px}
.logout{position:absolute;left:0;bottom:0;width:124px;height:26px;line-height:26px;background:var(--crimson);color:#fff;font-size:10px;padding-left:17px;display:flex;align-items:center;gap:4px}
.topbar{position:absolute;left:124px;top:0;right:0;height:35px;background:var(--bar)}
.page-title{position:absolute;left:23px;top:8px;font-size:12.5px;font-weight:500}
.search{position:absolute;left:277px;top:4px;width:173px;height:27px;border:1px solid #e4e4e4;border-radius:14px;background:#fff;font-size:7.5px;padding:8px 0 0 8px;color:#333}
.search svg{position:absolute;right:10px;top:8px}
.bell{position:absolute;left:456px;top:4px;width:27px;height:27px;border-radius:50%;background:#fff;box-shadow:0 1px 4px rgba(0,0,0,.12);display:flex;align-items:center;justify-content:center}
.avatar{position:absolute;left:488px;top:4px;width:27px;height:27px;border-radius:50%;background:linear-gradient(#c9b8ab,#8a1b2c)}
.user{position:absolute;left:521px;top:11px;font-size:10px}
.card{position:absolute;width:132px;height:173px;border:1px solid var(--line);background:#fff;text-align:center}
.card .shot{height:116px;background:#ececef}
.card .name{font-size:8.5px;font-weight:500;margin-top:9px;line-height:17px}
.card .price{font-size:8.5px;font-weight:500;color:var(--crimson);line-height:17px}
.card.hot .meta{background:var(--crimson);height:57px}
.card.hot .name,.card.hot .price{color:#fff}
.card.hot .name{margin-top:0;padding-top:9px}
.pager{position:absolute;left:374px;top:446px;font-size:8px;color:#aaa;display:flex;gap:6px;align-items:center}
.pager .cur{color:var(--crimson)}
.pager .arr{color:var(--navy);font-size:12px;margin:0 4px;line-height:8px}
.hero{position:absolute;left:144px;top:73px;width:290px;height:249px;background:#fff;box-shadow:0 2px 8px rgba(0,0,0,.12);padding:24px 30px}
.hero div{width:100%;height:100%;background:linear-gradient(#e6e6ea,#c9c9d0)}
.info{position:absolute;left:455px;top:88px;width:262px}
.info h1{font-size:19px;font-weight:600;color:var(--navy)}
.info .cost{font-size:12px;font-weight:600;color:var(--crimson)}
.info .label{font-size:9.5px;margin-top:5px}
.info .val{font-size:9.5px;margin-top:3px}
.qty{margin-top:6px;width:260px;height:31px;border:1px solid #cfcfcf;font-size:9.5px;display:flex;justify-content:space-between;align-items:center;padding:0 8px}
.info .spec{font-size:7.5px;color:var(--muted);line-height:17px;margin-top:5px}
.desc{position:absolute;left:144px;top:345px;width:580px}
.desc h2{font-size:9.5px;font-weight:500}
.desc p{font-size:7.5px;color:var(--muted);line-height:14.8px;margin-top:5px}
.cart-btn{position:absolute;left:318px;top:452px;width:235px;height:38px;background:var(--navy);color:#fff;font-size:12.5px;font-weight:600;display:flex;align-items:center;justify-content:center;box-shadow:0 3px 6px rgba(0,0,0,.2)}
</style>
</head>
<body>

<section class="screen list">
  <aside class="sidebar">
    <div class="brand"><span class="brand-dot"></span>Diamond Nine</div>
    <ul class="menu"><li>Home</li><li class="active">Products</li><li>Track my orders</li><li>My cart</li><li>Contact</li><li>Support</li><li>Help</li><li>Setting</li></ul>
    <div class="logout">Logout <svg width="9" height="8" viewBox="0 0 9 8"><path d="M1 1h3v6H1z" fill="none" stroke="#fff"/><path d="M4 4h4M6 2l2 2-2 2" fill="none" stroke="#fff"/></svg></div>
  </aside>
  <header class="topbar">
    <div class="page-title">All Products</div>
    <div class="search">Search Product<svg width="9" height="9" viewBox="0 0 9 9"><circle cx="3.8" cy="3.8" r="2.8" fill="none" stroke="#222" stroke-width="1.3"/><path d="M6 6l2.3 2.3" stroke="#222" stroke-width="1.3"/></svg></div>
    <div class="bell"><svg width="9" height="10" viewBox="0 0 9 10"><path d="M1.5 7.5h6L6.8 6.5V4a2.3 2.3 0 0 0-4.6 0v2.5z" fill="none" stroke="#ad0f33"/><path d="M3.7 9h1.6" stroke="#ad0f33"/></svg></div>
    <div class="avatar" role="img" aria-label="User profile photo"></div>
    <div class="user">Maren Castell</div>
  </header>

  <div class="card" style="left:144px;top:55px"><div class="shot" role="img" aria-label="Dark trucker hat photo" style="background:linear-gradient(#e2e2e6,#d4d4da)"></div><div class="meta"><div class="name">Salt Marlin Logo Hat</div><div class="price">12.000KD</div></div></div>
  <div class="card hot" style="left:294px;top:55px"><div class="shot" role="img" aria-label="Light grey printed t-shirt photo" style="background:linear-gradient(#f2f2f2,#dcdce0)"></div><div class="meta"><div class="name">Riverbend Flyway</div><div class="price">19.000KD</div></div></div>
  <div class="card" style="left:443px;top:55px"><div class="shot" role="img" aria-label="Black graphic t-shirt photo" style="background:linear-gradient(#f3f3f3,#e4e4e4)"></div><div class="meta"><div class="name">Island Surf Crew</div><div class="price">19.000KD</div></div></div>
  <div class="card" style="left:593px;top:55px"><div class="shot" role="img" aria-label="Blue patterned boonie hat photo" style="background:linear-gradient(#f7f7f7,#dde6ee)"></div><div class="meta"><div class="name">Reef Dive Boonie Hat</div><div class="price">20.000KD</div></div></div>

  <div class="card" style="left:144px;top:245px"><div class="shot" role="img" aria-label="Black boonie hat photo" style="background:linear-gradient(#fafafa,#ececec)"></div><div class="meta"><div class="name">Salt Marlin Patch Logo<br>Boonie Hat</div><div class="price">20.000KD</div></div></div>
  <div class="card" style="left:294px;top:245px"><div class="shot" role="img" aria-label="Mint graphic tee photo" style="background:linear-gradient(#f6f6f6,#d5efe8)"></div><div class="meta"><div class="name">Shoreline Graphic Tee</div><div class="price">19.000KD</div></div></div>
  <div class="card" style="left:443px;top:245px"><div class="shot" role="img" aria-label="Camo sleeve long-sleeve shirt photo" style="background:linear-gradient(#f1f2f6,#dcdfe8)"></div><div class="meta"><div class="name">Current Shift Long Sleeve</div><div class="price">20.000KD</div></div></div>
  <div class="card" style="left:593px;top:245px"><div class="shot" role="img" aria-label="Grey trucker cap photo" style="background:linear-gradient(#f4f4f4,#e2e3e6)"></div><div class="meta"><div class="name">Lake Mesh Cap</div><div class="price">13.000KD</div></div></div>

  <nav class="pager"><span class="arr">«</span><span class="cur">1</span><span>2</span><span>3</span><span>4</span><span>5</span><span>6</span><span>7</span><span>8</span><span>9</span><span class="arr">»</span></nav>
</section>

<section class="screen detail">
  <aside class="sidebar">
    <div class="brand"><span class="brand-dot"></span>Diamond Nine</div>
    <ul class="menu"><li>Home</li><li class="active">Products</li><li>Track my orders</li><li>My cart</li><li>Contact</li><li>Support</li><li>Help</li><li>Setting</li></ul>
    <div class="logout">Logout <svg width="9" height="8" viewBox="0 0 9 8"><path d="M1 1h3v6H1z" fill="none" stroke="#fff"/><path d="M4 4h4M6 2l2 2-2 2" fill="none" stroke="#fff"/></svg></div>
  </aside>
  <header class="topbar">
    <div class="page-title">All Products</div>
    <div class="search">Search Product<svg width="9" height="9" viewBox="0 0 9 9"><circle cx="3.8" cy="3.8" r="2.8" fill="none" stroke="#222" stroke-width="1.3"/><path d="M6 6l2.3 2.3" stroke="#222" stroke-width="1.3"/></svg></div>
    <div class="bell"><svg width="9" height="10" viewBox="0 0 9 10"><path d="M1.5 7.5h6L6.8 6.5V4a2.3 2.3 0 0 0-4.6 0v2.5z" fill="none" stroke="#ad0f33"/><path d="M3.7 9h1.6" stroke="#ad0f33"/></svg></div>
    <div class="avatar" role="img" aria-label="User profile photo"></div>
    <div class="user">Maren Castell</div>
  </header>

  <div class="hero"><div role="img" aria-label="Light grey printed t-shirt product photo"></div></div>
  <div class="info">
    <h1>Riverbend Flyway</h1>
    <div class="cost">19.000KD</div>
    <div class="label">Size</div>
    <div class="val">Large</div>
    <div class="label" style="margin-top:10px">Quantity</div>
    <div class="qty"><span>2</span><span>( - ) &nbsp;( + )</span></div>
    <div class="label" style="margin-top:12px">Specification</div>
    <p class="spec">Lorem ipsum dolor sit amet, consectetur adipiscing elit, sed do eiusmod tempor incididunt ut labore et dolore magna aliqua. Ut enim ad minim veniam, quis nostrud</p>
  </div>
  <div class="desc">
    <h2>Description</h2>
    <p>Lorem ipsum dolor sit amet, consectetur adipiscing elit, sed do eiusmod tempor incididunt ut labore et dolore magna aliqua. Ut enim ad minim veniam, quis nostrud exercitation ullamco laboris nisi ut aliquip ex ea commodo consequat. Duis aute irure dolor in reprehenderit in voluptate velit esse cillum dolore eu fugiat nulla pariatur. Excepteur sint occaecat cupidatat non proident, sunt in culpa qui officia deserunt mollit anim id est laborum Lorem ipsum dolor sit amet, consectetur adipiscing elit, sed do eiusmod tempor incididunt ut labore et dolore magna aliqua. Ut enim ad minim veniam, quis nostrud exercitation ullamco laboris nisi ut aliquip ex ea commodo consequat. Duis aute irure dolor</p>
  </div>
  <div class="cart-btn">Add To Cart</div>
</section>

</body>
</html>
```